Business Card & Logo Design Project

I am looking for a slick/simple design for a logo and business card, for a music Producer/Mixer/Engineer.

I'm based in Tokyo, Japan and I help my clients polish up their creation to major radio/TV status. My clients pay me for my taste, sense of balance expertise and creative direction/

Design should give impression of seal of quality, professionalism, and enthusiasm need some sort of a logo like design for "quorvane productions".

Please don't include music notes or instruments or anything musically related and anything samurai or ninja or too much Japan in them on the design.

I like clever, slick stuff that's not too obvious.
I also like a smooth gradation type transition. My favorite color is deep dark blue/

Good Luck and Thank you for your effort.
Updates

I would like a two-sided design for this one.
One side with "quorvane productions" (all lower case) on, and the other side with my name and contact info.

Please also consider portrait position (or direction).  (as opposed to landscape) 

Target Market(s)

My primary targets are artists & bands, who want absolute best for their creation.

Industry/Entity Type

Business

Requirements
Must have
• Two-Sided
1, quorvane productions
2, Kenji Harumoto, Producer/Mixer/Engineer, +81 000 0123 4567, brambleway@mailnest.example
Nice to have
• Any suggestions are welcome//
Should not have
• Anything music related images.
(e.g. CD, music notations, instruments etc.)

```html
<!DOCTYPE html>
<html lang="en">
<head>
<meta charset="utf-8">
<title>quorvane productions – business card</title>
<link rel="stylesheet" href="https://fonts.googleapis.com/css2?family=Orbitron:wght@400;500;600&family=Quicksand:wght@700&display=swap">
<style>
  :root {
    --accent: #e63b2e;
    --ink: #111111;
    --paper: #ffffff;
    --edge: #b5b5b5;
  }
  html, body {
    margin: 0;
    padding: 0;
    width: 1200px;
    height: 966px;
    overflow: hidden;
    background: var(--paper);
  }
  .canvas {
    position: relative;
    width: 1200px;
    height: 966px;
  }
  .card {
    position: absolute;
    width: 578px;
    height: 962px;
    box-sizing: border-box;
    border: 1px solid var(--edge);
    background: var(--paper);
  }
  .card--front { left: 0; top: 0; }
  .card--back { left: 620px; top: 2px; }
  .card svg {
    position: absolute;
    left: 0;
    top: 0;
    display: block;
  }

  .tech { font-family: "Orbitron", sans-serif; }
  .round { font-family: "Quicksand", sans-serif; }

  .brand-square { fill: var(--accent); }
  .brand-name { fill: var(--accent); font-weight: 600; font-size: 80px; }

  .back-brand__name { fill: var(--accent); font-weight: 600; font-size: 46px; }
  .back-brand__tag { fill: var(--ink); font-weight: 400; font-size: 25px; }
  .rule { fill: var(--accent); }

  .contact__name { fill: var(--accent); font-weight: 600; font-size: 48px; }
  .contact__role { fill: var(--accent); font-weight: 500; font-size: 22px; }
  .contact__phone { fill: var(--ink); font-weight: 500; font-size: 38px; }
  .contact__email { fill: var(--ink); font-weight: 700; font-size: 23px; }
</style>
</head>
<body>
<main class="canvas">
  <section class="card card--front" aria-label="Card front">
    <svg width="576" height="960" viewBox="0 0 576 960">
      <rect class="brand-square" x="229" y="392" width="120" height="120"/>
      <text class="tech brand-name" x="116" y="700" textLength="320" lengthAdjust="spacingAndGlyphs">quorvane</text>
    </svg>
  </section>

  <section class="card card--back" aria-label="Card back">
    <svg width="576" height="960" viewBox="0 0 576 960">
      <text class="tech back-brand__name" x="546" y="60" text-anchor="end" textLength="188" lengthAdjust="spacingAndGlyphs">quorvane</text>
      <rect class="rule" x="63" y="71" width="483" height="2"/>
      <text class="tech back-brand__tag" x="546" y="97" text-anchor="end" textLength="348" lengthAdjust="spacingAndGlyphs">productions</text>

      <text class="tech contact__name" x="546" y="442" text-anchor="end" textLength="396" lengthAdjust="spacingAndGlyphs">kenji harumoto</text>
      <text class="tech contact__role" x="546" y="470" text-anchor="end" textLength="318" lengthAdjust="spacingAndGlyphs">producer/mixer/engineer</text>
      <rect class="rule" x="120" y="479" width="426" height="2"/>
      <text class="tech contact__phone" x="546" y="529" text-anchor="end" textLength="398" lengthAdjust="spacingAndGlyphs">+81 000 0123 4567</text>
      <text class="round contact__email" x="544" y="553" text-anchor="end" textLength="300" lengthAdjust="spacingAndGlyphs">brambleway@mailnest.example</text>
    </svg>
  </section>
</main>
</body>
</html>
```